Our desktop web app builder needs a redesign

We want to redesign our low-code web app builder called Vorlix. Vorlix runs in desktop environments and is aimed at IT professionals and developers.

The UI consists of a button bar, multiple panels and a tabbed working area. We are looking to completely change the look and feel of the application interfaces, while keeping the layout and functionality the same.

We would like to see your ideas for fonts, sizing, colour, icons and any other visual UI element. Your work can be a rough mockup of your design ideas, and does not need to be pixel perfect. Legibility and optimised use of space are key.

More details about the app and how it works here: https://vorlix.example/

If we like your ideas, we will get in touch with you and work with you to develop the new design in greater detail.

```html
<!DOCTYPE html>
<html lang="en">
<head>
<meta charset="utf-8">
<title>Vorlix Designer</title>
<link href="https://fonts.googleapis.com/css2?family=Lato:wght@400;700&display=swap" rel="stylesheet">
<style>
:root{
  --accent:#1aa8c8;
  --accent-soft:#e1f3f8;
  --ink:#2b2b2b;
  --muted:#555a60;
  --icon:#4a4f57;
  --chrome:#f2f3f4;
  --panel:#f8f8f9;
  --header:#eceeef;
  --work:#eef0f2;
  --card:#f7f8f9;
  --green:#a8dcb0;
  --purple:#d9a6dd;
  --lavender:#c8c6ec;
  --grey-line:#c9ccd0;
  --select:#d3eef4;
  --select-line:#8fd3e3;
  --error:#e0302e;
  --validation:#e9e9ea;
}
*{box-sizing:border-box;margin:0;padding:0}
html,body{width:1200px;height:982px;overflow:hidden;background:#fff}
body{font-family:'Lato',sans-serif;color:var(--ink)}
.stage{position:absolute;left:0;top:0;width:1440px;height:1179px;transform:scale(.8333);transform-origin:0 0;overflow:hidden;background:#fff}
.abs{position:absolute}
.menubar{left:0;top:0;width:1440px;height:48px;background:var(--chrome)}
.brand{left:20px;top:16px;font-size:13px;font-weight:700;color:var(--accent)}
.menu{top:17px;font-size:12px;color:#333}
.doc-title{left:0;width:1440px;top:17px;text-align:center;font-size:12px;color:var(--accent)}
.toolbar{left:0;top:48px;width:1440px;height:50px;background:#fff;border-bottom:1px solid #e6e7e8}
.tool{top:48px;width:50px;height:50px;display:flex;align-items:center;justify-content:center}
.tool.run{background:var(--accent-soft)}
.dock-head{height:36px;background:var(--header)}
.dock-tab{height:36px;background:#fff;font-size:12px;font-weight:700;display:flex;align-items:center;padding-left:26px;color:#333}
.dock-ctrl{top:113px;display:flex;gap:14px}
.explorer{left:0;top:100px;width:268px;height:1079px;background:var(--panel)}
.tree{font-size:12px;color:#444}
.tree.active{color:var(--accent)}
.tree svg{position:absolute;left:-22px;top:-2px}
.workspace{left:270px;top:100px;width:896px;height:844px;background:var(--work)}
.canvas-card{left:294px;top:200px;width:860px;height:712px;background:var(--card)}
.frame{border:1px solid}
.frame-title{font-size:13px;color:var(--ink);background:var(--card);padding:0 10px 0 24px;height:18px;line-height:18px}
.frame-title svg{position:absolute;left:0;top:1px}
.field{height:34px;background:#fff;box-shadow:0 1px 2px rgba(0,0,0,.1);font-size:13px;display:flex;align-items:center;padding-left:42px;white-space:nowrap;overflow:hidden;color:#222}
.field svg{position:absolute;left:10px;top:7px}
.field.sel{border:1px solid var(--select-line);box-shadow:none}
.vsep{width:0;border-left:1px dashed #d5d7da}
.toolbox{left:1168px;top:100px;width:272px;height:1079px;background:var(--panel)}
.tb-item{width:60px;text-align:center;font-size:9px;color:#444;line-height:1.25;padding:0 6px}
.tb-item .glyph{display:block;margin:0 auto 8px;width:36px;height:44px;background:#f0f1f2;position:relative}
.validation{left:270px;top:944px;width:896px;height:235px;background:var(--validation)}
.v-row{left:296px;width:830px;height:29px;border-bottom:1px solid #dadadc;font-size:11.5px;color:#222;display:flex;align-items:center}
.v-row .x{color:var(--error);font-weight:700;width:16px;padding-left:2px}
.v-row .path{position:absolute;left:386px}
</style>
</head>
<body>
<div class="stage">

  <div class="abs menubar"></div>
  <div class="abs brand">Vorlix</div>
  <div class="abs menu" style="left:81px">File</div>
  <div class="abs menu" style="left:124px">Edit</div>
  <div class="abs menu" style="left:174px">Insert</div>
  <div class="abs menu" style="left:234px">Run</div>
  <div class="abs menu" style="left:284px">Windows</div>
  <div class="abs menu" style="left:363px">Help</div>
  <div class="abs doc-title">vorlixDesigner.xyz</div>

  <div class="abs toolbar"></div>
  <div class="abs tool" style="left:12px"><svg width="26" height="20"><path d="M2 4h8l2 2h10v3H7l-5 10z" fill="var(--icon)"/><path d="M7 10h18l-5 9H2z" fill="var(--icon)"/></svg></div>
  <div class="abs tool" style="left:63px"><svg width="20" height="20"><rect x="1" y="1" width="18" height="18" rx="2" fill="var(--icon)"/><rect x="5" y="2" width="10" height="6" fill="#fff"/><rect x="6" y="12" width="8" height="5" fill="#fff"/></svg></div>
  <div class="abs tool" style="left:115px"><svg width="18" height="22"><path d="M1 1h11l5 5v15H1z" fill="var(--icon)"/><path d="M4 9h10M4 12h10M4 15h10" stroke="#fff" stroke-width="1.3"/></svg></div>
  <div class="abs tool" style="left:163px"><svg width="20" height="22"><path d="M4 1h14l-2 20H1z" fill="var(--icon)"/><path d="M6 8h8M5 12h8M5 16h6" stroke="#fff" stroke-width="1.3"/></svg></div>
  <div class="abs tool" style="left:216px"><svg width="24" height="18"><g fill="var(--icon)"><rect x="0" y="1" width="3" height="3"/><rect x="6" y="1" width="18" height="3"/><rect x="0" y="7.5" width="3" height="3"/><rect x="6" y="7.5" width="18" height="3"/><rect x="0" y="14" width="3" height="3"/><rect x="6" y="14" width="18" height="3"/></g></svg></div>
  <div class="abs tool" style="left:269px"><svg width="20" height="20"><rect x="0" y="0" width="9" height="20" rx="2" fill="var(--icon)"/><rect x="11" y="0" width="9" height="9" rx="2" fill="var(--icon)"/><rect x="11" y="11" width="9" height="9" rx="2" fill="var(--icon)"/></svg></div>
  <div class="abs tool" style="left:320px"><svg width="22" height="18"><path d="M0 1h8l2 3h12v14H0z" fill="var(--icon)"/></svg></div>
  <div class="abs tool" style="left:371px"><svg width="20" height="22"><g fill="none" stroke="var(--icon)" stroke-width="2"><rect x="1" y="1" width="7" height="8"/><rect x="12" y="13" width="7" height="8"/></g><g fill="var(--icon)"><rect x="12" y="1" width="7" height="3"/><rect x="12" y="6" width="7" height="3"/><rect x="1" y="13" width="7" height="3"/><rect x="1" y="18" width="7" height="3"/></g></svg></div>
  <div class="abs tool" style="left:425px"><svg width="22" height="18"><rect x="1" y="1" width="20" height="16" fill="none" stroke="var(--icon)" stroke-width="2"/><g fill="var(--icon)"><rect x="4" y="5" width="6" height="3"/><rect x="12" y="5" width="6" height="3"/><rect x="4" y="10" width="6" height="3"/><rect x="12" y="10" width="6" height="3"/></g></svg></div>
  <div class="abs tool run" style="left:479px"><svg width="24" height="26"><path d="M2 1l21 12L2 25z" fill="var(--accent)"/></svg></div>
  <div class="abs tool" style="left:532px"><svg width="22" height="20"><path d="M0 2h8l2 3h12v15H0z" fill="var(--icon)"/><circle cx="11" cy="12.5" r="5" fill="#fff"/><path d="M11 15V10M8.8 12l2.2-2.2 2.2 2.2" stroke="var(--icon)" stroke-width="1.4" fill="none"/></svg></div>

  <div class="abs explorer"></div>
  <div class="abs dock-head" style="left:0;top:105px;width:268px"></div>
  <div class="abs dock-tab" style="left:0;top:105px;width:165px">Application Explorer</div>
  <div class="abs dock-ctrl" style="left:185px;top:113px">
    <svg width="16" height="16"><path d="M7 2H1v13h13V9" fill="none" stroke="#666" stroke-width="1.5"/><path d="M9 1h6v6M15 1L7 9" fill="none" stroke="#666" stroke-width="1.5"/></svg>
    <svg width="16" height="16"><path d="M5 1h6v2l-1 1v4l3 3H3l3-3V4L5 3zM8 11v5" fill="#666" stroke="#666"/></svg>
    <svg width="16" height="16"><path d="M2 2l12 12M14 2L2 14" stroke="#555" stroke-width="1.6"/></svg>
  </div>

  <svg class="abs" style="left:24px;top:150px" width="10" height="10"><path d="M1 3h8L5 8z" fill="var(--accent)"/></svg>
  <div class="abs tree active" style="left:69px;top:148px"><svg width="20" height="20"><rect x="3" y="1" width="14" height="6" fill="var(--accent)"/><path d="M10 7v4M4 11h12M4 11v4M10 11v4M16 11v4" stroke="var(--accent)" stroke-width="1.5"/><g fill="var(--accent)"><rect x="1" y="15" width="5" height="4"/><rect x="7.5" y="15" width="5" height="4"/><rect x="14" y="15" width="5" height="4"/></g></svg>Bugbear</div>
  <svg class="abs" style="left:47px;top:182px" width="10" height="10"><path d="M1 3h8L5 8z" fill="var(--accent)"/></svg>
  <div class="abs tree active" style="left:91px;top:180px"><svg width="16" height="18"><rect x="1" y="1" width="12" height="15" fill="none" stroke="var(--accent)" stroke-width="1.6"/><rect x="4" y="4" width="11" height="13" fill="var(--accent)"/></svg>Pages</div>
  <div class="abs" style="left:53px;top:202px;height:122px;border-left:1px solid var(--accent)"></div>
  <div class="abs" style="left:53px;top:324px;width:22px;border-top:1px solid var(--accent)"></div>
  <div class="abs" style="left:57px;top:222px;width:16px;border-top:1px dotted #999"></div>
  <div class="abs" style="left:57px;top:257px;width:16px;border-top:1px dotted #999"></div>
  <div class="abs" style="left:57px;top:289px;width:16px;border-top:1px dotted #999"></div>
  <svg class="abs" style="left:75px;top:218px" width="6" height="8"><path d="M0 0l5 4-5 4z" fill="#444"/></svg>
  <svg class="abs" style="left:75px;top:253px" width="6" height="8"><path d="M0 0l5 4-5 4z" fill="#444"/></svg>
  <svg class="abs" style="left:75px;top:285px" width="6" height="8"><path d="M0 0l5 4-5 4z" fill="#444"/></svg>
  <svg class="abs" style="left:75px;top:320px" width="6" height="8"><path d="M0 0l5 4-5 4z" fill="var(--accent)"/></svg>
  <div class="abs tree" style="left:113px;top:216px"><svg width="18" height="16"><path d="M1 2h6l2 2h8v11H1z" fill="var(--icon)"/></svg>Plox</div>
  <div class="abs tree" style="left:113px;top:251px"><svg width="14" height="16"><path d="M1 1h8l4 4v10H1z" fill="var(--icon)"/><path d="M3 8h8M3 11h8" stroke="#fff"/></svg>Addbug</div>
  <div class="abs tree" style="left:113px;top:283px"><svg width="14" height="16"><path d="M1 1h8l4 4v10H1z" fill="var(--icon)"/><path d="M3 8h8M3 11h8" stroke="#fff"/></svg>Home</div>
  <div class="abs tree active" style="left:113px;top:318px"><svg width="14" height="16"><path d="M1 1h8l4 4v10H1z" fill="var(--accent)"/><path d="M3 8h8M3 11h8" stroke="#fff"/></svg>Viewbug</div>
  <div class="abs tree" style="left:91px;top:354px"><svg width="18" height="18"><text x="4" y="14" font-size="14" font-family="Georgia,serif" font-weight="700" fill="var(--icon)">T</text><path d="M1 5V1h4M13 1h4v4M1 13v4h4M17 13v4h-4" stroke="var(--icon)" fill="none"/></svg>Types</div>
  <svg class="abs" style="left:49px;top:392px" width="6" height="8"><path d="M0 0l5 4-5 4z" fill="#555"/></svg>
  <div class="abs tree" style="left:91px;top:390px"><svg width="16" height="16"><rect x="0" y="0" width="7" height="16" rx="1" fill="var(--icon)"/><rect x="9" y="0" width="7" height="7" rx="1" fill="var(--icon)"/><rect x="9" y="9" width="7" height="7" rx="1" fill="var(--icon)"/></svg>Templates</div>
  <div class="abs tree" style="left:91px;top:427px"><svg width="16" height="16"><path d="M15 1L6 10l1 1 9-9zM5 11c-3 0-3 3-4 4 3 0 5-1 5-3z" fill="var(--icon)"/></svg>Styles</div>
  <div class="abs tree" style="left:91px;top:463px"><svg width="16" height="16"><circle cx="8" cy="8" r="5.5" fill="none" stroke="var(--icon)" stroke-width="3" stroke-dasharray="2.5 1.8"/><circle cx="8" cy="8" r="2" fill="var(--icon)"/></svg>Settings</div>
  <svg class="abs" style="left:49px;top:504px" width="6" height="8"><path d="M0 0l5 4-5 4z" fill="#555"/></svg>
  <div class="abs tree" style="left:91px;top:502px"><svg width="18" height="16"><path d="M1 2h6l2 2h8v11H1z" fill="var(--icon)"/></svg>Embedded files</div>
  <svg class="abs" style="left:49px;top:543px" width="6" height="8"><path d="M0 0l5 4-5 4z" fill="#555"/></svg>
  <div class="abs tree" style="left:91px;top:540px"><svg width="18" height="16"><path d="M4 10l6-5 5 2" stroke="var(--icon)" fill="none" stroke-width="1.5"/><circle cx="4" cy="10" r="3" fill="var(--icon)"/><circle cx="10" cy="5" r="2.5" fill="var(--icon)"/><circle cx="15" cy="7" r="2.5" fill="var(--icon)"/></svg>Connectors</div>

  <div class="abs workspace"></div>
  <div class="abs dock-tab" style="left:270px;top:103px;width:102px;height:37px;padding-left:14px;color:var(--accent)">View Bug</div>
  <div class="abs dock-ctrl" style="left:1084px">
    <svg width="16" height="16"><path d="M7 2H1v13h13V9" fill="none" stroke="#666" stroke-width="1.5"/><path d="M9 1h6v6M15 1L7 9" fill="none" stroke="#666" stroke-width="1.5"/></svg>
    <svg width="16" height="16"><path d="M5 1h6v2l-1 1v4l3 3H3l3-3V4L5 3zM8 11v5" fill="#666" stroke="#666"/></svg>
    <svg width="16" height="16"><path d="M2 2l12 12M14 2L2 14" stroke="#555" stroke-width="1.6"/></svg>
  </div>

  <div class="abs field" style="left:295px;top:155px;width:114px">
    <svg width="22" height="20"><text x="5" y="16" font-size="16" font-family="Georgia,serif" font-weight="700" fill="#333">T</text><path d="M1 5V1h4M17 1h4v4M1 15v4h4M21 15v4h-4" stroke="#333" fill="none" stroke-width="1.3"/></svg>Label 1</div>

  <div class="abs canvas-card"></div>

  <div class="abs frame" style="left:314px;top:231px;width:816px;height:654px;border-color:var(--green)"></div>
  <div class="abs frame-title" style="left:334px;top:222px"><svg width="18" height="15"><rect x=".5" y=".5" width="16" height="13" fill="none" stroke="#8fd39a"/><path d="M.5 5h16M.5 9.5h16M6 .5v13M11 .5v13" stroke="#8fd39a"/></svg>Layout Table 1</div>
  <div class="abs" style="left:341px;top:240px;font-size:10px;color:#555">↳</div>

  <div class="abs frame" style="left:342px;top:266px;width:594px;height:588px;border-color:var(--purple)"></div>
  <div class="abs frame-title" style="left:360px;top:257px;padding-right:14px"><svg width="16" height="16"><g fill="#c07ac7"><rect x="0" y="0" width="6" height="4"/><rect x="0" y="6" width="6" height="4"/><rect x="0" y="12" width="6" height="4"/><rect x="8" y="0" width="8" height="4" opacity=".6"/><rect x="8" y="6" width="8" height="4" opacity=".6"/><rect x="8" y="12" width="8" height="4" opacity=".6"/></g></svg>Detail Panel</div>
  <div class="abs" style="left:368px;top:274px;font-size:10px;color:#555">↳</div>

  <div class="abs frame" style="left:369px;top:298px;width:551px;height:142px;border-color:var(--lavender)"></div>
  <div class="abs frame-title" style="left:391px;top:289px"><svg width="18" height="15"><rect x=".5" y=".5" width="16" height="13" fill="none" stroke="#8b8fe0"/><path d="M.5 5h16M.5 9.5h16M6 .5v13M11 .5v13" stroke="#8b8fe0"/></svg>Layout Table 2</div>
  <div class="abs vsep" style="left:525px;top:324px;height:90px"></div>
  <div class="abs vsep" style="left:673px;top:324px;height:90px"></div>
  <div class="abs vsep" style="left:821px;top:324px;height:90px"></div>
  <div class="abs" style="left:380px;top:369px;width:540px;border-top:1px dashed #d5d7da"></div>

  <div class="abs field" style="left:387px;top:326px;width:128px"><svg width="22" height="20"><text x="5" y="16" font-size="16" font-family="Georgia,serif" font-weight="700" fill="#333">T</text><path d="M1 5V1h4M17 1h4v4M1 15v4h4M21 15v4h-4" stroke="#333" fill="none" stroke-width="1.3"/></svg>Label 3</div>
  <div class="abs field" style="left:535px;top:326px;width:128px"><svg width="22" height="20"><text x="5" y="16" font-size="16" font-family="Georgia,serif" font-weight="700" fill="#333">T</text><path d="M1 5V1h4M17 1h4v4M1 15v4h4M21 15v4h-4" stroke="#333" fill="none" stroke-width="1.3"/></svg>Reported by L</div>
  <div class="abs field" style="left:683px;top:326px;width:128px"><svg width="22" height="20"><text x="5" y="16" font-size="16" font-family="Georgia,serif" font-weight="700" fill="#333">T</text><path d="M1 5V1h4M17 1h4v4M1 15v4h4M21 15v4h-4" stroke="#333" fill="none" stroke-width="1.3"/></svg>Label 2</div>
  <div class="abs field" style="left:387px;top:380px;width:128px"><svg width="22" height="20"><text x="2" y="11" font-size="12" font-family="Georgia,serif" fill="#333">T</text><path d="M15 1h4v4M1 15v4h4M19 15v4h-4" stroke="#333" fill="none" stroke-width="1.3"/></svg>Reported on</div>
  <div class="abs field" style="left:535px;top:380px;width:128px"><svg width="22" height="20"><text x="2" y="11" font-size="12" font-family="Georgia,serif" fill="#333">T</text><path d="M15 1h4v4M1 15v4h4M19 15v4h-4" stroke="#333" fill="none" stroke-width="1.3"/></svg>Reported byT</div>
  <div class="abs field" style="left:683px;top:380px;width:128px"><svg width="22" height="20"><text x="2" y="11" font-size="12" font-family="Georgia,serif" fill="#333">T</text><path d="M15 1h4v4M1 15v4h4M19 15v4h-4" stroke="#333" fill="none" stroke-width="1.3"/></svg>StatusDrop</div>
  <div class="abs field" style="left:831px;top:380px;width:88px;padding-left:35px"><svg width="20" height="18"><rect x="1" y="1" width="17" height="15" fill="none" stroke="#333" stroke-width="1.4"/><path d="M3 14l5-6 4 4 2-2 3 4z" fill="#333"/><circle cx="13" cy="5" r="1.6" fill="#333"/></svg>Plox Imag</div>

  <div class="abs frame" style="left:369px;top:476px;width:551px;height:344px;border-color:#d9dbe7"></div>
  <div class="abs frame-title" style="left:393px;top:467px"><svg width="18" height="18"><g fill="#9a9ef0"><rect x="0" y="0" width="4.5" height="4.5"/><rect x="6" y="0" width="4.5" height="4.5"/><rect x="12" y="0" width="4.5" height="4.5"/><rect x="0" y="6" width="4.5" height="4.5"/><rect x="6" y="6" width="4.5" height="4.5"/><rect x="12" y="6" width="4.5" height="4.5"/><rect x="0" y="12" width="4.5" height="4.5"/><rect x="6" y="12" width="4.5" height="4.5"/><rect x="12" y="12" width="4.5" height="4.5"/></g></svg>Layout Grid</div>
  <div class="abs" style="left:400px;top:485px;font-size:10px;color:#555">↳</div>

  <div class="abs frame" style="left:401px;top:511px;width:455px;height:81px;border-color:var(--grey-line)"></div>
  <div class="abs frame-title" style="left:416px;top:502px"><svg width="18" height="15"><rect x=".5" y=".5" width="16" height="13" fill="none" stroke="#444"/><path d="M.5 5h16M.5 9.5h16M6 .5v13M11 .5v13" stroke="#444"/></svg>Layout Table 3</div>
  <div class="abs vsep" style="left:555px;top:533px;height:36px"></div>
  <div class="abs vsep" style="left:703px;top:533px;height:36px"></div>
  <div class="abs field" style="left:417px;top:533px;width:128px"><svg width="22" height="20"><text x="5" y="16" font-size="16" font-family="Georgia,serif" font-weight="700" fill="#333">T</text><path d="M1 5V1h4M17 1h4v4M1 15v4h4M21 15v4h-4" stroke="#333" fill="none" stroke-width="1.3"/></svg>Label 3</div>
  <div class="abs field" style="left:565px;top:533px;width:128px"><svg width="22" height="20"><text x="5" y="16" font-size="16" font-family="Georgia,serif" font-weight="700" fill="#333">T</text><path d="M1 5V1h4M17 1h4v4M1 15v4h4M21 15v4h-4" stroke="#333" fill="none" stroke-width="1.3"/></svg>Reported by L</div>
  <div class="abs field" style="left:713px;top:533px;width:128px"><svg width="22" height="20"><text x="5" y="16" font-size="16" font-family="Georgia,serif" font-weight="700" fill="#333">T</text><path d="M1 5V1h4M17 1h4v4M1 15v4h4M21 15v4h-4" stroke="#333" fill="none" stroke-width="1.3"/></svg>Label 2</div>

  <div class="abs field" style="left:402px;top:604px;width:128px"><svg width="22" height="20"><text x="5" y="16" font-size="16" font-family="Georgia,serif" font-weight="700" fill="#333">T</text><path d="M1 5V1h4M17 1h4v4M1 15v4h4M21 15v4h-4" stroke="#333" fill="none" stroke-width="1.3"/></svg>Title TexBox</div>

  <div class="abs" style="left:385px;top:669px;width:483px;height:104px;background:var(--select)"></div>
  <div class="abs frame" style="left:401px;top:682px;width:455px;height:81px;border-color:var(--select-line)"></div>
  <div class="abs frame-title" style="left:416px;top:673px;background:var(--select);color:var(--accent)"><svg width="18" height="15"><rect x=".5" y=".5" width="16" height="13" fill="none" stroke="var(--accent)"/><path d="M.5 5h16M.5 9.5h16M6 .5v13M11 .5v13" stroke="var(--accent)"/></svg>Layout Table 4</div>
  <div class="abs vsep" style="left:555px;top:704px;height:36px;border-color:#a9d9e4"></div>
  <div class="abs vsep" style="left:703px;top:704px;height:36px;border-color:#a9d9e4"></div>
  <div class="abs field sel" style="left:417px;top:704px;width:128px"><svg width="22" height="20"><text x="5" y="16" font-size="16" font-family="Georgia,serif" font-weight="700" fill="#333">T</text><path d="M1 5V1h4M17 1h4v4M1 15v4h4M21 15v4h-4" stroke="#333" fill="none" stroke-width="1.3"/></svg>Label 3</div>
  <div class="abs field sel" style="left:565px;top:704px;width:128px"><svg width="22" height="20"><text x="5" y="16" font-size="16" font-family="Georgia,serif" font-weight="700" fill="#333">T</text><path d="M1 5V1h4M17 1h4v4M1 15v4h4M21 15v4h-4" stroke="#333" fill="none" stroke-width="1.3"/></svg>Reported by L</div>
  <div class="abs field sel" style="left:713px;top:704px;width:128px"><svg width="22" height="20"><text x="5" y="16" font-size="16" font-family="Georgia,serif" font-weight="700" fill="#333">T</text><path d="M1 5V1h4M17 1h4v4M1 15v4h4M21 15v4h-4" stroke="#333" fill="none" stroke-width="1.3"/></svg>Label 2</div>

  <div class="abs field" style="left:402px;top:775px;width:126px"><svg width="22" height="20"><text x="2" y="11" font-size="12" font-family="Georgia,serif" fill="#333">T</text><path d="M15 1h4v4M1 15v4h4M19 15v4h-4" stroke="#333" fill="none" stroke-width="1.3"/></svg>Description</div>

  <div class="abs frame" style="left:950px;top:266px;width:160px;height:266px;border-color:var(--purple)"></div>
  <div class="abs frame-title" style="left:970px;top:257px;padding-right:14px"><svg width="16" height="16"><g fill="#c07ac7"><rect x="0" y="0" width="6" height="4"/><rect x="0" y="6" width="6" height="4"/><rect x="0" y="12" width="6" height="4"/><rect x="8" y="0" width="8" height="4" opacity=".6"/><rect x="8" y="6" width="8" height="4" opacity=".6"/><rect x="8" y="12" width="8" height="4" opacity=".6"/></g></svg>Panel 1</div>
  <div class="abs" style="left:964px;top:342px;width:130px;border-top:1px dashed #d5d7da"></div>
  <div class="abs" style="left:964px;top:397px;width:130px;border-top:1px dashed #d5d7da"></div>
  <div class="abs" style="left:964px;top:452px;width:130px;border-top:1px dashed #d5d7da"></div>
  <div class="abs field" style="left:965px;top:299px;width:128px"><svg width="22" height="20"><text x="5" y="16" font-size="16" font-family="Georgia,serif" font-weight="700" fill="#333">T</text><path d="M1 5V1h4M17 1h4v4M1 15v4h4M21 15v4h-4" stroke="#333" fill="none" stroke-width="1.3"/></svg>Label 3</div>
  <div class="abs field" style="left:965px;top:353px;width:128px"><svg width="22" height="20"><text x="2" y="11" font-size="12" font-family="Georgia,serif" fill="#333">T</text><path d="M15 1h4v4M1 15v4h4M19 15v4h-4" stroke="#333" fill="none" stroke-width="1.3"/></svg>Reported on</div>
  <div class="abs field" style="left:965px;top:408px;width:128px"><svg width="22" height="20"><text x="2" y="11" font-size="12" font-family="Georgia,serif" fill="#333">T</text><path d="M15 1h4v4M1 15v4h4M19 15v4h-4" stroke="#333" fill="none" stroke-width="1.3"/></svg>Reported on</div>
  <div class="abs field" style="left:965px;top:463px;width:128px"><svg width="22" height="20"><text x="2" y="11" font-size="12" font-family="Georgia,serif" fill="#333">T</text><path d="M15 1h4v4M1 15v4h4M19 15v4h-4" stroke="#333" fill="none" stroke-width="1.3"/></svg>Reported on</div>

  <div class="abs toolbox"></div>
  <div class="abs dock-head" style="left:1168px;top:100px;width:272px;height:37px"></div>
  <div class="abs dock-tab" style="left:1168px;top:100px;width:100px;height:37px">Tool Box</div>
  <div class="abs dock-ctrl" style="left:1355px;top:111px">
    <svg width="16" height="16"><path d="M7 2H1v13h13V9" fill="none" stroke="#666" stroke-width="1.5"/><path d="M9 1h6v6M15 1L7 9" fill="none" stroke="#666" stroke-width="1.5"/></svg>
    <svg width="16" height="16"><path d="M5 1h6v2l-1 1v4l3 3H3l3-3V4L5 3zM8 11v5" fill="#666" stroke="#666"/></svg>
    <svg width="16" height="16"><path d="M2 2l12 12M14 2L2 14" stroke="#555" stroke-width="1.6"/></svg>
  </div>

  <div class="abs tb-item" style="left:1170px;top:183px"><span class="glyph" role="img" aria-label="Tap gesture icon"></span>Button</div>
  <div class="abs tb-item" style="left:1234px;top:183px"><span class="glyph" role="img" aria-label="Tap gesture icon"></span>Chart</div>
  <div class="abs tb-item" style="left:1298px;top:183px"><span class="glyph" role="img" aria-label="Tap gesture icon"></span>Checkbox</div>
  <div class="abs tb-item" style="left:1362px;top:183px"><span class="glyph" role="img" aria-label="Tap gesture icon"></span>Checkbox List</div>
  <div class="abs tb-item" style="left:1170px;top:268px"><span class="glyph" role="img" aria-label="Tap gesture icon"></span>Data Grid</div>
  <div class="abs tb-item" style="left:1234px;top:268px"><span class="glyph" role="img" aria-label="Tap gesture icon"></span>View</div>
  <div class="abs tb-item" style="left:1298px;top:268px"><span class="glyph" role="img" aria-label="Tap gesture icon"></span>View</div>
  <div class="abs tb-item" style="left:1362px;top:268px"><span class="glyph" role="img" aria-label="Tap gesture icon"></span>View</div>
  <div class="abs tb-item" style="left:1170px;top:353px"><span class="glyph" role="img" aria-label="Tap gesture icon"></span>View</div>
  <div class="abs tb-item" style="left:1234px;top:353px"><span class="glyph" role="img" aria-label="Tap gesture icon"></span>View</div>
  <div class="abs tb-item" style="left:1298px;top:353px"><span class="glyph" role="img" aria-label="Tap gesture icon"></span>View</div>
  <div class="abs tb-item" style="left:1362px;top:353px"><span class="glyph" role="img" aria-label="Tap gesture icon"></span>View</div>
  <div class="abs tb-item" style="left:1170px;top:438px"><span class="glyph" role="img" aria-label="Tap gesture icon"></span></div>
  <div class="abs tb-item" style="left:1234px;top:438px"><span class="glyph" role="img" aria-label="Tap gesture icon"></span></div>
  <div class="abs tb-item" style="left:1298px;top:438px"><span class="glyph" role="img" aria-label="Tap gesture icon"></span></div>
  <div class="abs tb-item" style="left:1362px;top:438px"><span class="glyph" role="img" aria-label="Tap gesture icon"></span></div>

  <div class="abs dock-head" style="left:1168px;top:690px;width:272px"></div>
  <div class="abs dock-tab" style="left:1168px;top:690px;width:165px">Propeties DataG</div>
  <div class="abs dock-ctrl" style="left:1355px;top:700px">
    <svg width="16" height="16"><path d="M7 2H1v13h13V9" fill="none" stroke="#666" stroke-width="1.5"/><path d="M9 1h6v6M15 1L7 9" fill="none" stroke="#666" stroke-width="1.5"/></svg>
    <svg width="16" height="16"><path d="M5 1h6v2l-1 1v4l3 3H3l3-3V4L5 3zM8 11v5" fill="#666" stroke="#666"/></svg>
    <svg width="16" height="16"><path d="M2 2l12 12M14 2L2 14" stroke="#555" stroke-width="1.6"/></svg>
  </div>

  <div class="abs validation"></div>
  <div class="abs dock-head" style="left:270px;top:944px;width:896px;background:#e2e3e5"></div>
  <div class="abs dock-tab" style="left:270px;top:944px;width:116px;background:#ececed">Validation</div>
  <div class="abs dock-ctrl" style="left:1080px;top:954px">
    <svg width="16" height="16"><path d="M7 2H1v13h13V9" fill="none" stroke="#666" stroke-width="1.5"/><path d="M9 1h6v6M15 1L7 9" fill="none" stroke="#666" stroke-width="1.5"/></svg>
    <svg width="16" height="16"><path d="M5 1h6v2l-1 1v4l3 3H3l3-3V4L5 3zM8 11v5" fill="#666" stroke="#666"/></svg>
    <svg width="16" height="16"><path d="M2 2l12 12M14 2L2 14" stroke="#555" stroke-width="1.6"/></svg>
  </div>
  <div class="abs" style="left:296px;top:1003px;font-size:13.5px">Description</div>
  <div class="abs" style="left:652px;top:1002px;font-size:13px;color:#666">|</div>
  <div class="abs" style="left:682px;top:1003px;font-size:13.5px">Path</div>
  <div class="abs v-row" style="top:1024px"><span class="x">x</span>No page has been link<span class="path">C:\Program Files (x86)\MORVANE Software\Download Navigator</span></div>
  <div class="abs v-row" style="top:1053px"><span class="x">x</span>No page has been link<span class="path">C:\Program Files (x86)\MORVANE Software</span></div>
  <div class="abs v-row" style="top:1082px"><span class="x">x</span>No page has been link<span class="path">C:\Program Files (x86)\MORVANE Software</span></div>
  <div class="abs v-row" style="top:1112px"><span class="x">x</span>No page has been link<span class="path">C:\Program Files (x86)\MORVANE Software</span></div>

</div>
</body>
</html>
```